Company or website name
- Harwood & Beale LLP
- Links to the website
- harwoodbeale-example.com
- Describe your company and organization and target audience
- lawyers and clients in the need of lawyer for defective products etc
- The design should have the following
- yes
- Other Facts

```html
<!DOCTYPE html>
<html lang="en">
<head>
<meta charset="utf-8">
<title>Harwood &amp; Beale LLP</title>
<link href="https://fonts.googleapis.com/css2?family=Arimo:wght@400;700&display=swap" rel="stylesheet">
<style>
:root{
  --navy:#16266a;
  --navy-deep:#0c1a52;
  --ink:#222;
  --muted:#555;
  --page:#fff;
  --rule:#14286b;
  --footer:#4b4e53;
  --footer-text:#a9abae;
  --shade:#7d7d7d;
}
*{box-sizing:border-box;margin:0;padding:0}
html,body{width:961px;height:1200px;overflow:hidden}
body{background:var(--page);font-family:"Arimo",Arial,sans-serif;position:relative}
.page{position:absolute;left:43px;top:0;width:874px;height:1200px;background:var(--page);
  box-shadow:-14px 0 16px -6px var(--shade),14px 0 16px -6px var(--shade)}
.abs{position:absolute}
.brand{left:26px;top:34px;font-size:27px;font-weight:700;color:var(--navy);letter-spacing:.5px;white-space:nowrap}
.brand-mark{left:24px;top:8px;width:96px;height:96px;border-radius:50%;background:#eef0f4;z-index:0}
.brand{z-index:1}
.search{left:636px;top:37px;width:160px;height:19px;border:2.5px solid var(--navy-deep);border-radius:10px}
.search-icon{left:797px;top:31px}
.nav a{position:absolute;top:73px;height:30px;line-height:30px;font-size:18px;font-weight:700;color:var(--navy-deep);text-decoration:none}
.nav .active{left:271px;width:81px;text-align:center;color:#fff;border-radius:15px;
  background:linear-gradient(#3a5aa6,var(--navy-deep));font-size:20px}
.rule{background:var(--rule);left:0;width:874px}
.hero-art{left:154px;top:137px;width:186px;height:200px;border-radius:6px;
  background:radial-gradient(ellipse at 50% 45%,#f3d57a,#c99a2e 55%,#fff 75%)}
.hero-title{left:354px;top:191px;width:470px;font-size:21px;line-height:24px;font-weight:700;color:var(--navy)}
.btn{background:linear-gradient(#3b5db0,var(--navy-deep));color:#fff;font-weight:700;border-radius:20px;text-align:center;border:2px solid #9fb0d8}
.hero-btn{left:405px;top:265px;width:163px;height:36px;line-height:32px;font-size:23px}
.welcome{left:63px;top:358px;font-size:18px;font-weight:700;color:#444}
.copy{color:var(--navy);font-weight:700;text-transform:uppercase}
.intro p{font-size:14px;line-height:17px;width:400px}
.intro .indent{text-indent:61px}
.login{left:559px;top:386px;width:252px;height:166px;background:#fdfdfd}
.login h2{position:absolute;left:7px;top:4px;font-size:15px;font-weight:700;color:#222}
.login label{position:absolute;left:6px;font-size:15px;color:#222}
.login .field{position:absolute;left:81px;width:167px;height:21px;border:1px solid #c9c9c9;background:#fff}
.login .submit{position:absolute;left:7px;top:107px;width:53px;height:21px;border:1px solid #999;border-radius:2px;
  background:linear-gradient(#fafafa,#d9d9d9);font-size:13px;text-align:center;line-height:19px;color:#222}
.feature .copy{position:absolute;left:71px;width:450px;font-size:14px;line-height:17px}
.photo{position:absolute;left:549px;width:256px;height:137px;overflow:hidden}
.photo .fill{position:absolute;inset:0}
.photo .caption{position:absolute;left:0;bottom:0;width:100%;height:24px;background:linear-gradient(#2a4a9a,var(--navy-deep));
  color:#fff;font-weight:700;font-size:17px;line-height:24px;padding-left:24px}
.photo .tag{position:absolute;right:5px;top:4px;height:22px;line-height:19px;padding:0 9px;font-size:12px;border-radius:11px}
.scales{background:linear-gradient(#6f7478,#c9cdd0 55%,#53595d)}
.gavel{background:linear-gradient(120deg,#b9895a,#6a3a1a 50%,#e0c7a0)}
.footer{left:0;top:1111px;width:874px;height:89px;background:var(--footer)}
.footer nav a{position:absolute;top:30px;font-size:14px;font-weight:700;color:var(--footer-text);text-decoration:none}
.footer .line{position:absolute;left:80px;top:60px;width:760px;height:1px;background:#5c5f64}
.footer .legal{position:absolute;right:98px;top:69px;font-size:10px;color:#8a8d91}
.social{position:absolute;top:20px;width:31px;height:31px;border:2px solid #ddd;border-radius:50%}
</style>
</head>
<body>
<div class="page">
  <header>
    <div class="abs brand-mark" aria-hidden="true"></div>
    <div class="abs brand">Harwood &amp; Beale LLP</div>
    <div class="abs search" role="search" aria-label="Search"></div>
    <svg class="abs search-icon" width="32" height="32" viewBox="0 0 32 32" aria-hidden="true">
      <circle cx="12" cy="12" r="8" fill="none" stroke="#0c1a52" stroke-width="4"/>
      <line x1="18" y1="18" x2="28" y2="28" stroke="#0c1a52" stroke-width="5" stroke-linecap="round"/>
    </svg>
    <nav class="nav">
      <a class="active" href="#">HOME</a>
      <a href="#" style="left:374px">NEWS</a>
      <a href="#" style="left:457px">SERVICE</a>
      <a href="#" style="left:563px">ABOUT</a>
      <a href="#" style="left:666px">HELP</a>
      <a href="#" style="left:745px">CONTACT US</a>
    </nav>
  </header>
  <div class="abs rule" style="top:114px;height:7px"></div>

  <section class="hero">
    <div class="abs hero-art" role="img" aria-label="Golden scales of justice"></div>
    <h1 class="abs hero-title">LOREM IPSUM IS SIMPLY DUMMY TEXT OF THE PRINTING AND TYPESETTING INDUSTRY</h1>
    <div class="abs btn hero-btn">READ MORE</div>
  </section>

  <section class="intro">
    <h2 class="abs welcome">You've come to the right place.</h2>
    <p class="abs copy indent" style="left:67px;top:392px">Lorem ipsum is simply dummy text of the printing and typesetting industry. Lorem ipsum has been the industry's standard dummy text ever since the 1500</p>
    <p class="abs copy indent" style="left:67px;top:465px">Lorem ipsum is simply dummy text of the printing and typesetting industry. Lorem ipsum has been the industry's standard dummy text ever since the 1500</p>
    <p class="abs copy" style="left:64px;top:543px;font-size:12.5px;line-height:15px;width:420px">Lorem ipsum is simply dummy text of the printing and typesetting industry. Lorem ipsum has been the industry's standard dummy text ever since the 1500</p>
    <form class="abs login" aria-label="Customer Login">
      <h2>Customer Login</h2>
      <label style="top:47px">Username</label><div class="field" style="top:45px"></div>
      <label style="top:69px">Password</label><div class="field" style="top:67px"></div>
      <div class="submit">Login</div>
    </form>
  </section>

  <div class="abs rule" style="top:590px;height:9px"></div>

  <section class="feature">
    <p class="copy" style="top:652px">Lorem ipsum is simply dummy text of the printing and typesetting industry. Lorem ipsum has been the industry's standard dummy text ever since the 1500</p>
    <div class="photo" style="top:616px">
      <div class="fill scales" role="img" aria-label="Balance scale silhouetted against a cloudy sky"></div>
      <div class="btn tag">READ MORE</div>
      <div class="caption">LOREM IPSUM</div>
    </div>
  </section>
  <div class="abs rule" style="top:763px;height:9px;left:-2px;width:880px"></div>

  <section class="feature">
    <p class="copy" style="top:825px">Lorem ipsum is simply dummy text of the printing and typesetting industry. Lorem ipsum has been the industry's standard dummy text ever since the 1500</p>
    <div class="photo" style="top:790px">
      <div class="fill gavel" role="img" aria-label="Wooden gavel in front of brass scales"></div>
      <div class="btn tag">READ MORE</div>
      <div class="caption">LOREM IPSUM</div>
    </div>
  </section>
  <div class="abs rule" style="top:936px;height:9px;left:-2px;width:880px"></div>

  <section class="feature">
    <p class="copy" style="top:998px">Lorem ipsum is simply dummy text of the printing and typesetting industry. Lorem ipsum has been the industry's standard dummy text ever since the 1500</p>
    <div class="photo" style="top:963px">
      <div class="fill scales" role="img" aria-label="Balance scale silhouetted against a cloudy sky"></div>
      <div class="btn tag">READ MORE</div>
      <div class="caption">LOREM IPSUM</div>
    </div>
  </section>

  <footer class="abs footer">
    <nav>
      <a href="#" style="left:40px;color:#777">HOME</a>
      <a href="#" style="left:148px">NEWS</a>
      <a href="#" style="left:265px">SERVICE</a>
      <a href="#" style="left:384px">ABOUT</a>
      <a href="#" style="left:503px">HELP</a>
      <a href="#" style="left:594px">CONTACT US</a>
    </nav>
    <svg class="social" style="left:688px;border:none" width="31" height="31" viewBox="0 0 31 31" aria-label="Email">
      <circle cx="15.5" cy="15.5" r="14" fill="none" stroke="#ddd" stroke-width="2"/>
      <rect x="9" y="11" width="13" height="9" rx="1.5" fill="#ddd"/>
      <path d="M9 11.5l6.5 5 6.5-5" fill="none" stroke="#4b4e53" stroke-width="1.2"/>
    </svg>
    <div class="social" style="left:725px" aria-label="Social profile"></div>
    <div class="social" style="left:762px" aria-label="Social profile"></div>
    <div class="line"></div>
    <div class="legal">Privacy Policy &nbsp;|&nbsp; Terms and Conditions &nbsp;|&nbsp; © 2014</div>
  </footer>
</div>
</body>
</html>
```